Single-page, simple & clean, departure board web app

TrellWick.com provides easy to use train schedule information in Chicago, IL between downtown and Hyde Park. The site has been around for about 3 years and the design has not changed since the weekend hackathon at which it was created. Now, it has a solid user base and is in dire need of a fresh design.
The design should be super-clean and intuitive. It is used by the type of people who love the style and personality of sites like Dazzleferr. The design should incorporate the maroon color that is used extensively on the existing site. The main features are (1) the train depart times, (2) the fact that different stations can be selected as departure/arrival, (3) the fact that a user can click "earlier trains" or "later trains" to quickly scan the times.
This is a single-page web app that displays static content. The design should reflect that 100% of the users time is spent on the single page. There is no "sign up" process or external aspect. All focus should be used to design the best possible display of train times.
Target Market(s)
24-30 yr old, middle to upper income, opinionated, heavily international
Look and feel
Each slider illustrates characteristics of the customer's brand and the style your logo design should communicate.

```html
<!DOCTYPE html>
<html lang="en">
<head>
<meta charset="utf-8">
<title>TrellWick – Train Schedule</title>
<link href="https://fonts.googleapis.com/css2?family=Arimo:wght@400;700&display=swap" rel="stylesheet">
<style>
:root{
  --maroon:#a3283e;
  --maroon-dark:#891d31;
  --maroon-text:#9e2339;
  --panel:#e8e8e8;
  --rule:#cfcfcf;
  --ink:#3a3a3a;
  --ad-blue:#1d5fae;
  --white:#fff;
}
*{box-sizing:border-box;margin:0;padding:0}
html,body{width:903px;height:1200px;overflow:hidden;background:var(--white)}
body{font-family:"Arimo",Arial,sans-serif;color:var(--ink);position:relative}
.masthead{position:absolute;left:32px;top:14px;width:840px;height:65px;border-radius:4px;
  background:linear-gradient(#b4344b,var(--maroon-dark));color:var(--white);display:flex;align-items:center}
.brand{font-size:25px;font-weight:700;padding-left:19px;width:246px;letter-spacing:.3px}
.tagline{border-left:1px solid rgba(255,255,255,.3);padding-left:13px;font-size:11.5px;line-height:16px;height:38px;display:flex;flex-direction:column;justify-content:center;color:#f3dde1}
.like-box{margin-left:auto;margin-right:16px;background:rgba(0,0,0,.12);border:1px solid rgba(255,255,255,.25);border-radius:3px;height:22px;display:flex;align-items:center;gap:5px;padding:0 6px;font-size:8px}
.like-btn{background:#eee;color:#333;border-radius:2px;padding:2px 4px;display:flex;align-items:center;gap:3px}
.like-btn i{width:7px;height:7px;background:#777;display:block}
.section-head{position:absolute;left:32px;width:840px;height:41px;border-top:1px solid var(--rule);border-bottom:1px solid var(--rule);display:flex;align-items:center}
.section-head h2{font-size:18px;font-weight:400;color:var(--maroon-text);padding-left:19px;width:347px}
.pager{font-size:12px;color:#444;display:flex;align-items:center;gap:7px}
.pager.later{margin-left:auto;margin-right:27px}
.pager svg{width:8px;height:12px}
.select{position:absolute;height:21px;border:1px solid #d4d4d4;border-radius:2px;background:linear-gradient(#fafafa,#ececec);font-size:11px;color:#444;display:flex;align-items:center;padding:0 14px}
.select::after{content:"";margin-left:auto;border-left:4px solid transparent;border-right:4px solid transparent;border-top:7px solid #444}
.train{position:absolute;left:48px;width:807px;height:122px;display:flex}
.train-id{width:272px;background:var(--panel);display:flex;align-items:center;justify-content:center;font-size:18.5px;color:var(--maroon-text);border-right:2px solid var(--white)}
.stops{flex:1;display:flex;flex-direction:column;gap:2px}
.stop{flex:1;background:var(--panel);display:flex;align-items:center;font-size:12.5px;color:#555}
.stop .kind{width:62px;padding-left:26px;box-sizing:content-box}
.stop .sep{width:32px;color:#999;font-size:10px}
.stop .time{width:93px}
.stop.depart .kind,.stop.depart .time{font-weight:700;color:#222}
.stop.depart .sep{color:#222}
.ad{position:absolute;left:133px;top:1060px;width:624px;height:77px;background:var(--ad-blue);display:flex;align-items:center;color:var(--white);overflow:hidden}
.ad-slogan{width:136px;flex:none;text-align:center;font-size:10px;font-weight:700;line-height:20px}
.ad-slogan b{display:block;background:var(--white);color:var(--ad-blue);margin:0 5px}
.ad-items{width:356px;flex:none;height:61px;background:var(--white);border-radius:3px;display:flex;padding:4px}
.ad-item{flex:1;color:#222;font-size:8.5px;padding:0 3px}
.ad-item h3{font-weight:400;text-align:center;font-size:8.5px;color:var(--ad-blue);border-bottom:2px solid var(--ad-blue);margin-bottom:4px}
.ad-item .row{display:flex;align-items:center;gap:4px}
.ad-item .pic{width:52px;height:36px;border-radius:3px;background:linear-gradient(#c9c9c9,#8a8a8a)}
.ad-item .price{font-size:7px;line-height:11px}
.ad-item .price strong{font-size:9px;display:block}
.ad-mascot{width:42px;flex:none;height:54px;margin-left:8px;border-radius:6px;background:linear-gradient(#9ab7db,#4f7cb6)}
.ad-name{display:flex;align-items:center;gap:4px;font-size:12px;font-weight:700;margin-left:6px;white-space:nowrap}
.ad-name i{width:10px;height:10px;border-radius:50%;background:var(--white);display:block}
.ad-code{position:absolute;left:849px;top:1133px;font-size:8px;color:#444}
.footer{position:absolute;left:32px;top:1146px;width:840px;height:42px;border-radius:4px;background:linear-gradient(#b4344b,var(--maroon-dark));color:#f3dde1;font-size:10px;display:flex;align-items:center;justify-content:space-between;padding:0 17px}
</style>
</head>
<body>
<header class="masthead">
  <div class="brand">TrellWick</div>
  <div class="tagline"><span>Lakeline Electric between Downtown Chicago and Hollis Booth</span><span>Designed for home, school, and mobile access</span></div>
  <div class="like-box"><span class="like-btn"><i></i>Like</span><span>110 people like this.</span></div>
</header>

<div class="section-head" style="top:95px">
  <h2>To Hollis Booth</h2>
  <a class="pager"><svg viewBox="0 0 8 12"><path d="M6.5 1 1.5 6l5 5" fill="none" stroke="#8c1f33" stroke-width="2.2"/></svg>earlier trains</a>
  <a class="pager later">later trains<svg viewBox="0 0 8 12"><path d="M1.5 1l5 5-5 5" fill="none" stroke="#8c1f33" stroke-width="2.2"/></svg></a>
</div>
<div class="select" style="left:70px;top:146px;width:141px">From Millenium</div>
<div class="select" style="left:225px;top:146px;width:108px">From 11 th</div>

<section class="train" style="top:178px"><div class="train-id">Train #8303</div><div class="stops">
<div class="stop depart"><span class="kind">Depart</span><span class="sep">:</span><span class="time">5:00 am</span><span>from Millennium Station</span></div>
<div class="stop"><span class="kind">Arrive</span><span class="sep">:</span><span class="time">5:13 am</span><span>at 51st-53rd Street</span></div>
<div class="stop"><span class="kind">Arrive</span><span class="sep">:</span><span class="time">5:15 am</span><span>at 55th-56th-57th Street</span></div>
<div class="stop"><span class="kind">Arrive</span><span class="sep">:</span><span class="time">5:17 am</span><span>at 59th Street</span></div></div></section>
<section class="train" style="top:308px"><div class="train-id">Train #8303</div><div class="stops">
<div class="stop depart"><span class="kind">Depart</span><span class="sep">:</span><span class="time">5:00 am</span><span>from Millennium Station</span></div>
<div class="stop"><span class="kind">Arrive</span><span class="sep">:</span><span class="time">5:13 am</span><span>at 51st-53rd Street</span></div>
<div class="stop"><span class="kind">Arrive</span><span class="sep">:</span><span class="time">5:15 am</span><span>at 55th-56th-57th Street</span></div>
<div class="stop"><span class="kind">Arrive</span><span class="sep">:</span><span class="time">5:17 am</span><span>at 59th Street</span></div></div></section>
<section class="train" style="top:439px"><div class="train-id">Train #8303</div><div class="stops">
<div class="stop depart"><span class="kind">Depart</span><span class="sep">:</span><span class="time">5:00 am</span><span>from Millennium Station</span></div>
<div class="stop"><span class="kind">Arrive</span><span class="sep">:</span><span class="time">5:13 am</span><span>at 51st-53rd Street</span></div>
<div class="stop"><span class="kind">Arrive</span><span class="sep">:</span><span class="time">5:15 am</span><span>at 55th-56th-57th Street</span></div>
<div class="stop"><span class="kind">Arrive</span><span class="sep">:</span><span class="time">5:17 am</span><span>at 59th Street</span></div></div></section>

<div class="section-head" style="top:577px">
  <h2>To Downtown</h2>
  <a class="pager"><svg viewBox="0 0 8 12"><path d="M6.5 1 1.5 6l5 5" fill="none" stroke="#8c1f33" stroke-width="2.2"/></svg>earlier trains</a>
  <a class="pager later">later trains<svg viewBox="0 0 8 12"><path d="M1.5 1l5 5-5 5" fill="none" stroke="#8c1f33" stroke-width="2.2"/></svg></a>
</div>
<div class="select" style="left:70px;top:627px;width:141px">From 59th</div>

<section class="train" style="top:662px"><div class="train-id">Train #8303</div><div class="stops">
<div class="stop depart"><span class="kind">Depart</span><span class="sep">:</span><span class="time">5:00 am</span><span>from Millennium Station</span></div>
<div class="stop"><span class="kind">Arrive</span><span class="sep">:</span><span class="time">5:13 am</span><span>at 51st-53rd Street</span></div>
<div class="stop"><span class="kind">Arrive</span><span class="sep">:</span><span class="time">5:15 am</span><span>at 55th-56th-57th Street</span></div>
<div class="stop"><span class="kind">Arrive</span><span class="sep">:</span><span class="time">5:17 am</span><span>at 59th Street</span></div></div></section>
<section class="train" style="top:793px"><div class="train-id">Train #8303</div><div class="stops">
<div class="stop depart"><span class="kind">Depart</span><span class="sep">:</span><span class="time">5:00 am</span><span>from Millennium Station</span></div>
<div class="stop"><span class="kind">Arrive</span><span class="sep">:</span><span class="time">5:13 am</span><span>at 51st-53rd Street</span></div>
<div class="stop"><span class="kind">Arrive</span><span class="sep">:</span><span class="time">5:15 am</span><span>at 55th-56th-57th Street</span></div>
<div class="stop"><span class="kind">Arrive</span><span class="sep">:</span><span class="time">5:17 am</span><span>at 59th Street</span></div></div></section>
<section class="train" style="top:925px"><div class="train-id">Train #8303</div><div class="stops">
<div class="stop depart"><span class="kind">Depart</span><span class="sep">:</span><span class="time">5:00 am</span><span>from Millennium Station</span></div>
<div class="stop"><span class="kind">Arrive</span><span class="sep">:</span><span class="time">5:13 am</span><span>at 51st-53rd Street</span></div>
<div class="stop"><span class="kind">Arrive</span><span class="sep">:</span><span class="time">5:15 am</span><span>at 55th-56th-57th Street</span></div>
<div class="stop"><span class="kind">Arrive</span><span class="sep">:</span><span class="time">5:17 am</span><span>at 59th Street</span></div></div></section>

<aside class="ad">
  <div class="ad-slogan"><b>SELL IT ALL TODAY</b>www.swapnest.in</div>
  <div class="ad-items">
    <div class="ad-item"><h3>Rovan 80</h3><div class="row"><div class="pic" role="img" aria-label="Photo of a small red hatchback car"></div><div class="price">FROM<strong>₹ 50,000</strong></div></div></div>
    <div class="ad-item"><h3>Kamvio</h3><div class="row"><div class="pic" role="img" aria-label="Photo of a black digital camera"></div><div class="price">FROM<strong>₹ 5,000</strong></div></div></div>
    <div class="ad-item"><h3>Dining Table</h3><div class="row"><div class="pic" role="img" aria-label="Photo of a wooden dining table set"></div><div class="price">FROM<strong>₹ 2,000</strong></div></div></div>
  </div>
  <div class="ad-mascot" role="img" aria-label="Cartoon computer mascot illustration"></div>
  <div class="ad-name"><i></i>Swapnest</div>
</aside>
<div class="ad-code">X22</div>

<footer class="footer">
  <span>Train Schedule Last Updated: January 15, 2012</span>
  <span>terms and conditions of use | questions or comments</span>
</footer>
</body>
</html>
```